Layout für Longboardshop
Zielgruppe
Online Shop für Longboards, basierend auf Ladenwerk 4.1.2
Zielgruppe: Sportliche Menschen mit Hang zum Wellenreiten, Surfen,Kiten, Snowboarden oder Skateboarden.
Aufgabenstellung
Erstellung des Grunddesigns (Header, Footer, Menü, Detailansicht, Buttons) als PSD. Die Umsetzung in ein Template erledigen wir alleine.
Neugründung: Es existieren noch keine Logos oder Farbvorgaben.
We have no site, it is a completly new project. There are no limits concerning colors, fonts etc.
Competitors:
http://www.brettfahrer-welt.de
http://wilhelmine-bretter.de/
http://www.rollbrettladen.de/
http://www.kavero.de/de_DE/Skateboard/Longboards.html?sid=1
http://www.pirumo-bretter.de/
I think, big pictures transporting the surfstyle attitude of this sport works good.
Der Grundaufbau sollte sich an http://www.ladenwerkdemo.de/ anlehnen, um den Anpassungsaufwand mgl. überschaubar zu halten.

```html
<!DOCTYPE html>
<html lang="de">
<head>
<meta charset="utf-8">
<title>Rollwelle-Markt – Longboardshop</title>
<link href="https://fonts.googleapis.com/css2?family=Source+Sans+3:wght@300;400;600;700&display=swap" rel="stylesheet">
<style>
:root{
  --teal:#1b9cc4;
  --teal-dark:#0d7aa3;
  --ink:#222;
  --text:#444;
  --muted:#666;
  --bar:#2f2f2f;
  --page:#ebebeb;
  --panel:#d3d3d3;
  --line:#dcdcdc;
  --btn-grey:#4a4a4a;
  --footer:#333;
  --footer-bottom:#1a6e96;
}
*{box-sizing:border-box;margin:0;padding:0}
html,body{width:1200px;height:1200px;overflow:hidden}
body{position:relative;background:var(--page);font-family:"Source Sans 3","Source Sans Pro",sans-serif;color:var(--text)}
.abs{position:absolute}

/* top bar */
.topbar{left:0;top:0;width:1200px;height:22px;background:var(--bar)}
.topbar .item{position:absolute;top:0;height:22px;display:flex;align-items:center;gap:6px;color:#ddd;font-size:7px;border-left:1px solid #444;padding-left:10px}
.topbar svg{width:10px;height:10px}
.search{position:absolute;left:769px;top:3px;width:169px;height:15px;background:#fafafa;border-radius:2px;font-size:6.5px;color:#999;padding:3px 8px}
.search .mag{position:absolute;right:0;top:0;width:16px;height:15px;border-left:1px solid #ccc;display:flex;align-items:center;justify-content:center}

/* header */
.logo{left:470px;top:60px;width:260px;text-align:center;font-weight:700;font-size:28px;line-height:32px;color:var(--ink);letter-spacing:-0.5px;white-space:nowrap}
.cart{left:790px;top:45px;width:171px;height:54px;background:#f6f6f6;border:1px solid #ddd}
.cart .bag{position:absolute;left:11px;top:4px;width:22px;height:28px}
.cart .label{position:absolute;left:42px;top:15px;font-size:8.5px;font-weight:600;color:#333}
.cart .sep{position:absolute;left:112px;top:6px;width:1px;height:26px;background:#ccc}
.cart .total{position:absolute;left:118px;top:9px;width:50px;text-align:center;font-size:7.5px;line-height:10px;color:#555}
.cart .total b{font-weight:700}
.cart .info{position:absolute;left:0;top:40px;width:171px;text-align:center;font-size:7.5px;color:#444}
.cart .info a{color:var(--teal-dark);text-decoration:none}

/* nav + hero */
.stage{left:240px;top:120px;width:720px;height:310px;background:#fff}
.nav{left:308px;top:126px;width:652px;height:23px;display:flex;background:linear-gradient(var(--teal),var(--teal-dark))}
.nav a{flex:none;display:flex;align-items:center;justify-content:center;color:#fff;font-size:8.5px;font-weight:600;text-decoration:none;border-right:1px solid #0b6d92}
.nav a:last-child{border-right:0}
.home-tab{left:248px;top:128px;width:51px;height:19px;border:1px solid var(--teal);color:var(--teal-dark);font-size:8.5px;font-weight:600;display:flex;align-items:center;justify-content:center}
.hero{left:247px;top:166px;width:706px;height:258px;background:linear-gradient(120deg,#1c3a4c 0%,#2f6687 45%,#4d88a8 70%,#223f52 100%)}
.hero-text{left:265px;top:184px;width:141px;color:#fff}
.hero-text .l1{font-weight:300;font-size:26px;line-height:26px;letter-spacing:-0.8px;white-space:nowrap}
.hero-text .l2{font-weight:700;font-size:37px;line-height:33px;letter-spacing:-1.2px;white-space:nowrap}
.hero-text p{margin-top:11px;font-size:7.6px;line-height:17.4px;text-align:justify;color:#e8eef2;font-weight:300}
.hero-corner{left:900px;top:371px;width:53px;height:53px}
.hero-shadow{left:300px;top:430px;width:600px;height:3px;background:radial-gradient(ellipse at center,rgba(0,0,0,.35),rgba(0,0,0,0) 70%)}

/* sidebar */
.sidebar{left:240px;top:450px;width:169px;height:485px;background:var(--panel)}
.fhead{position:absolute;left:7px;width:154px;height:23px;background:linear-gradient(var(--teal),var(--teal-dark));color:#fff;font-size:8.5px;font-weight:600;display:flex;align-items:center;justify-content:center}
.flist{position:absolute;left:7px;width:154px}
.flist li{list-style:none;height:24px;background:#fff;border-bottom:1px solid var(--line);display:flex;align-items:center;font-size:8px;color:#555}
.box{width:10px;height:10px;border:1px solid #ccc;border-radius:2px;margin:0 20px 0 22px;background:#f5f5f5;display:flex;align-items:center;justify-content:center}
.flist li.on{font-size:9.5px;color:#333}
.price{position:absolute;left:7px;top:279px;width:154px;height:71px;background:#fff;font-size:7.5px;color:#444}
.btn-reset{left:240px;top:948px;width:51px;height:30px;background:var(--btn-grey);display:flex;align-items:center;justify-content:center}
.btn-filter{left:297px;top:948px;width:112px;height:30px;background:linear-gradient(var(--teal),var(--teal-dark));color:#fff;font-size:8.5px;font-weight:600;display:flex;align-items:center;justify-content:center}

/* products */
.products{left:420px;top:450px;width:540px;height:528px;background:var(--panel)}
.card{position:absolute;width:122px;height:217px;background:#fff;border:1px solid #c8c8c8}
.card .img{position:absolute;left:10px;top:10px;width:100px;height:135px}
.card h3{position:absolute;left:0;top:153px;width:100%;text-align:center;font-size:11px;font-weight:400;color:#111;letter-spacing:-0.2px}
.card .desc{position:absolute;left:0;top:167px;width:100%;text-align:center;font-size:7.5px;line-height:10.5px;color:#333}
.card .btns{position:absolute;left:3px;top:194px;display:flex;gap:3px}
.card .det{width:36px;height:18px;background:var(--btn-grey);color:#eee;font-size:6.5px;display:flex;align-items:center;justify-content:center}
.card .add{width:77px;height:18px;background:linear-gradient(var(--teal),var(--teal-dark));color:#fff;font-size:6.5px;font-weight:600;display:flex;align-items:center;justify-content:center}
.pager{position:absolute;width:25px;height:22px;background:#fff;border:1px solid #ccc;display:flex;align-items:center;justify-content:center}

/* footer */
.footer{left:0;top:1037px;width:1200px;height:138px;background:var(--footer);border-top:2px solid var(--teal)}
.fcol{position:absolute;top:1064px;color:#ddd;font-size:8px}
.fcol h4{font-weight:400;font-size:8.5px;color:#fff;margin-bottom:18px}
.fcol h4 span{color:var(--teal)}
.fcol .grid{display:grid;row-gap:0}
.fcol .grid div{height:15.6px}
.fcol a{color:var(--teal);text-decoration:none}
.fcol p{font-size:8px;line-height:15.6px;text-align:justify}
.bottom{left:0;top:1175px;width:1200px;height:25px;background:var(--footer-bottom);color:#eee;font-size:7.5px;display:flex;align-items:center;justify-content:center}
</style>
</head>
<body>

<header>
  <div class="abs topbar">
    <div class="item" style="left:407px;width:82px">
      <svg viewBox="0 0 10 10"><circle cx="5" cy="3" r="2.3" fill="#ddd"/><path d="M1 10c0-3 2-4.5 4-4.5s4 1.5 4 4.5z" fill="#ddd"/></svg>Mein Konto</div>
    <div class="item" style="left:489px;width:77px">
      <svg viewBox="0 0 10 10"><rect x="1.5" y="1" width="7" height="8.5" fill="none" stroke="#ddd"/><path d="M3 5l1.5 1.5L7 3.5" fill="none" stroke="#ddd"/></svg>Merkzettel</div>
    <div class="item" style="left:566px;width:83px">
      <svg viewBox="0 0 10 10"><path d="M1 1l8 8M9 1L1 9" stroke="#ddd" stroke-width="1.6"/></svg>Service/Hilfe</div>
    <div class="item" style="left:649px;width:52px">
      <svg viewBox="0 0 10 10"><path d="M2 3.5l3 3 3-3" fill="none" stroke="#ddd" stroke-width="1.5"/></svg>EUR</div>
    <div class="item" style="left:701px;width:48px">
      <svg viewBox="0 0 10 10"><path d="M2 3.5l3 3 3-3" fill="none" stroke="#ddd" stroke-width="1.5"/></svg>
      <svg viewBox="0 0 12 8" style="width:12px;height:8px"><rect width="12" height="2.7" fill="#111"/><rect y="2.7" width="12" height="2.7" fill="#d00"/><rect y="5.4" width="12" height="2.6" fill="#fc0"/></svg></div>
    <div class="item" style="left:749px;width:210px;border-right:1px solid #444"></div>
    <div class="search">Suchbegriff eingeben
      <span class="mag"><svg viewBox="0 0 10 10" width="7" height="7"><circle cx="6" cy="4" r="3" fill="none" stroke="#666"/><path d="M4 6L1 9" stroke="#666" stroke-width="1.3"/></svg></span></div>
  </div>

  <div class="abs logo">rollwelle-markt.de</div>

  <div class="abs cart">
    <svg class="bag" viewBox="0 0 22 28"><path d="M3 8h16l1 19H2z" fill="#b9c7cf"/><path d="M7 9V5a4 4 0 0 1 8 0v4" fill="none" stroke="#8fa2ad"/></svg>
    <div class="label">WARENKORB</div>
    <div class="sep"></div>
    <div class="total">Total:<br><b>84,95€</b></div>
    <div class="info">Es befinden sich <a href="#">2 Artikel</a> im Warenkorb.</div>
  </div>
</header>

<div class="abs stage"></div>
<div class="abs home-tab">HOME</div>
<nav class="abs nav">
  <a href="#" style="width:107px">DECKS</a>
  <a href="#" style="width:112px">ZUBEHÖR</a>
  <a href="#" style="width:105px">% SALE</a>
  <a href="#" style="width:91px">TEAM</a>
  <a href="#" style="width:109px">BILDER</a>
  <a href="#" style="width:128px">KONTAKT</a>
</nav>

<div class="abs hero" role="img" aria-label="Photo of longboard skaters rolling down a street towards the sea, blue toned"></div>
<div class="abs hero-text">
  <div class="l1">DIE NEUSTEN</div>
  <div class="l2">BOARDS<br>IM TEST!</div>
  <p>Lorem quis bibendum auctor, nisi elit consequat ipsum, nec sagittis sem nibh id elit. Duis sed odio sit amet nibh vulputate cursus a sit amet mauris. Morbi accumsan ipsum velit. Nam nec tellus a odio tincidunt auctor a ornare odio. Sed non mauris vitae erat conse.</p>
</div>
<svg class="abs hero-corner" viewBox="0 0 53 53"><path d="M53 0V53H0z" fill="#fff"/><path d="M51 3V51H3" fill="none" stroke="#1d3442" stroke-width="1.5"/><path d="M31 32l4 4-4 4M36 32l4 4-4 4" fill="none" stroke="#111" stroke-width="1.8"/></svg>
<div class="abs hero-shadow"></div>

<aside class="abs sidebar">
  <div class="fhead" style="top:5px">MARKE</div>
  <ul class="flist" style="top:32px">
    <li><span class="box"></span>Auswahl #1</li>
    <li class="on"><span class="box"><svg viewBox="0 0 8 8" width="7" height="7"><path d="M1 4l2 2 4-4" fill="none" stroke="#1a6e96" stroke-width="1.4"/></svg></span>Auswahl #2</li>
    <li><span class="box"></span>Auswahl #3</li>
    <li><span class="box"></span>Auswahl #4</li>
    <li><span class="box"></span>Auswahl #5</li>
    <li><span class="box"></span>Auswahl #6</li>
    <li><span class="box"></span>Auswahl #7</li>
    <li><span class="box"></span>Auswahl #8</li>
    <li><span class="box"></span>Auswahl #9</li>
  </ul>
  <div class="fhead" style="top:252px">PREISKLASSE</div>
  <div class="price">
    <span class="abs" style="left:40px;top:19px">100€</span>
    <span class="abs" style="left:99px;top:18px">200€</span>
    <svg class="abs" style="left:16px;top:30px" width="120" height="12" viewBox="0 0 120 12">
      <line x1="2" y1="6" x2="118" y2="6" stroke="#555" stroke-width="1.5"/>
      <g stroke="#777"><line x1="2" y1="2" x2="2" y2="10"/><line x1="31" y1="2" x2="31" y2="10"/><line x1="60" y1="2" x2="60" y2="10"/><line x1="89" y1="2" x2="89" y2="10"/><line x1="118" y1="2" x2="118" y2="10"/></g>
      <circle cx="60" cy="6" r="3" fill="#fff" stroke="#777"/></svg>
    <span class="abs" style="left:8px;top:46px">&lt;50€</span>
    <span class="abs" style="left:69px;top:44px;font-size:9.5px;font-weight:600">150€</span>
    <span class="abs" style="left:125px;top:46px">250€&lt;</span>
  </div>
  <div class="fhead" style="top:357px">ZUBEHÖR</div>
  <ul class="flist" style="top:383px">
    <li><span class="box"></span>Auswahl #1</li>
    <li class="on"><span class="box"><svg viewBox="0 0 8 8" width="7" height="7"><path d="M1 4l2 2 4-4" fill="none" stroke="#1a6e96" stroke-width="1.4"/></svg></span>Auswahl #2</li>
    <li><span class="box"></span>Auswahl #3</li>
    <li><span class="box"></span>Auswahl #4</li>
  </ul>
</aside>
<div class="abs btn-reset"><svg width="16" height="16" viewBox="0 0 16 16"><path d="M8 2a6 6 0 1 1-5.6 4" fill="none" stroke="#fff" stroke-width="1.8"/><path d="M1 3l2 4 3-3z" fill="#fff"/></svg></div>
<div class="abs btn-filter">FILTER STARTEN</div>

<main class="abs products">
  <div class="card" style="left:8px;top:5px"><div class="img" role="img" aria-label="Two longboard decks, one black and one colourful pattern" style="background:linear-gradient(90deg,#444 0 45%,#fff 45% 55%,#3fa3b8 55%)"></div><h3>ARTIKELBEZEICHNUNG</h3><div class="desc">Lorem Ipsum. Proin gravidanv.<br>Preis: <b>123,00€</b> inkl. MwSt.</div><div class="btns"><span class="det">DETAILS</span><span class="add">IN DEN WARENKORB</span></div></div>
  <div class="card" style="left:141px;top:5px"><div class="img" role="img" aria-label="Two wooden longboard decks" style="background:linear-gradient(90deg,#fff 0 20%,#c9a16b 20% 45%,#fff 45% 55%,#b8875a 55% 80%,#fff 80%)"></div><h3>ARTIKELBEZEICHNUNG</h3><div class="desc">Lorem Ipsum. Proin gravidanv.<br>Preis: <b>123,00€</b> inkl. MwSt.</div><div class="btns"><span class="det">DETAILS</span><span class="add">IN DEN WARENKORB</span></div></div>
  <div class="card" style="left:276px;top:5px"><div class="img" role="img" aria-label="Grey skate helmet" style="background:radial-gradient(circle at 50% 45%,#888 0 38%,#fff 40%)"></div><h3>ARTIKELBEZEICHNUNG</h3><div class="desc">Lorem Ipsum. Proin gravidanv.<br>Preis: <b>123,00€</b> inkl. MwSt.</div><div class="btns"><span class="det">DETAILS</span><span class="add">IN DEN WARENKORB</span></div></div>
  <div class="card" style="left:411px;top:5px"><div class="img" role="img" aria-label="Two longboard decks in green, yellow and red stripes" style="background:linear-gradient(#2e8f3e 0 33%,#d8c33a 33% 66%,#c8392c 66%)"></div><h3>ARTIKELBEZEICHNUNG</h3><div class="desc">Lorem Ipsum. Proin gravidanv.<br>Preis: <b>123,00€</b> inkl. MwSt.</div><div class="btns"><span class="det">DETAILS</span><span class="add">IN DEN WARENKORB</span></div></div>

  <div class="card" style="left:8px;top:260px"><div class="img" role="img" aria-label="Silver longboard truck" style="background:radial-gradient(ellipse at 50% 45%,#b5b5b5 0 30%,#fff 45%)"></div><h3>ARTIKELBEZEICHNUNG</h3><div class="desc">Lorem Ipsum. Proin gravidanv.<br>Preis: <b>123,00€</b> inkl. MwSt.</div><div class="btns"><span class="det">DETAILS</span><span class="add">IN DEN WARENKORB</span></div></div>
  <div class="card" style="left:141px;top:260px"><div class="img" role="img" aria-label="Stack of skate bearings" style="background:radial-gradient(ellipse at 50% 50%,#4a9bc4 0 18%,#333 20% 42%,#fff 48%)"></div><h3>ARTIKELBEZEICHNUNG</h3><div class="desc">Lorem Ipsum. Proin gravidanv.<br>Preis: <b>123,00€</b> inkl. MwSt.</div><div class="btns"><span class="det">DETAILS</span><span class="add">IN DEN WARENKORB</span></div></div>
  <div class="card" style="left:276px;top:260px"><div class="img" role="img" aria-label="Two longboard decks, black and printed" style="background:linear-gradient(90deg,#fff 0 18%,#3a3a3a 18% 45%,#fff 45% 55%,#5a4a30 55% 82%,#fff 82%)"></div><h3>ARTIKELBEZEICHNUNG</h3><div class="desc">Lorem Ipsum. Proin gravidanv.<br>Preis: <b>123,00€</b> inkl. MwSt.</div><div class="btns"><span class="det">DETAILS</span><span class="add">IN DEN WARENKORB</span></div></div>
  <div class="card" style="left:411px;top:260px"><div class="img" role="img" aria-label="White skate wheel with black print" style="background:radial-gradient(circle at 50% 45%,#ddd 0 40%,#fff 42%)"></div><h3>ARTIKELBEZEICHNUNG</h3><div class="desc">Lorem Ipsum. Proin gravidanv.<br>Preis: <b>123,00€</b> inkl. MwSt.</div><div class="btns"><span class="det">DETAILS</span><span class="add">IN DEN WARENKORB</span></div></div>

  <div class="pager" style="left:238px;top:494px"><svg width="12" height="10" viewBox="0 0 12 10"><path d="M6 1L2 5l4 4M11 1L7 5l4 4" fill="none" stroke="#111" stroke-width="1.8"/></svg></div>
  <div class="pager" style="left:276px;top:494px"><svg width="12" height="10" viewBox="0 0 12 10"><path d="M1 1l4 4-4 4M6 1l4 4-4 4" fill="none" stroke="#1b9cc4" stroke-width="1.8"/></svg></div>
</main>

<footer>
  <div class="abs footer"></div>
  <div class="fcol" style="left:240px">
    <h4><span>ROLLWELLE-MARKT.DE</span> SITEMAP</h4>
    <div class="grid" style="grid-template-columns:43px 43px 60px">
      <div>Home</div><div>Team</div><div>Mein Konto</div>
      <div>Decks</div><div>Bilder</div><div>Datenschutz</div>
      <div>Zubehör</div><div>Kontakt</div><div>Merkzettel</div>
      <div>Sale</div><div>AGB</div><div>Impressum</div>
    </div>
  </div>
  <div class="fcol" style="left:454px">
    <h4><span>ROLLWELLE-MARKT.DE</span> KONTAKT</h4>
    <div class="grid" style="grid-template-columns:108px 140px">
      <div style="font-weight:600;color:#fff">rollwelle-markt.de</div><div>T: 12345 - 67 89 01 12 34</div>
      <div>Longboardstraße 1</div><div>F: 12345 - 67 89 02 12 35</div>
      <div>12345 Longboardstadt</div><div>M: <a href="#">info@rollwelle-markt.de</a></div>
      <div>Deutschland</div><div>W: <a href="#">www.rollwelle-markt.de</a></div>
    </div>
  </div>
  <div class="fcol" style="left:750px;width:211px">
    <h4><span>ROLLWELLE-MARKT.DE</span> VERSANDINFOS</h4>
    <p>Lorem Ipsum. Proin gravida nibh vel velit auctor aliquet. Aenean sollicitudin, lorem quis bibendum auctor, nisi elit consequat ipsum, nec sagittis sem nibh id elit. Duis sed odio sit amet nibh vulputate cursus a sit amet mauris.</p>
  </div>
  <div class="abs bottom">Copyright © 2013 Longboardname &nbsp;|&nbsp; Alle Rechte vorbehalten.</div>
</footer>

</body>
</html>
```